Kestrim LLC, needs a web page no more than 5 pages (for now)

Kestrim is a general contractor. Our services include general contracting, design-build construction, disaster recovery and environmental remediation. Our main clients are KZE, HJ, State and Local Gov't Agencies, Hospitals and Schools. Kestrim is also a SDVOSB.

```html
<!DOCTYPE html>
<html lang="en">
<head>
<meta charset="utf-8">
<title>Kestrim LLC — General Contractor</title>
<link href="https://fonts.googleapis.com/css2?family=Inter:wght@400;500;600;700;800&display=swap" rel="stylesheet">
<style>
:root{
  --blue:#2563eb;--green:#16a34a;--red:#dc2626;--purple:#9333ea;
  --navy:#0f172a;--ink:#0f172a;--text:#475569;--muted:#64748b;
  --soft:#f8fafc;--hero:#e6eefc;--gold:#b8912f;--white:#fff;
}
*{box-sizing:border-box;margin:0;padding:0}
html,body{width:1200px;height:5195px;overflow:hidden}
body{font-family:'Inter',sans-serif;color:var(--ink);background:var(--white);position:relative}
.abs{position:absolute}
.logo{display:flex;align-items:center;gap:8px;font-weight:700;font-size:20px;color:var(--gold)}
.logo-dot{width:14px;height:14px;border-radius:50%;background:var(--gold)}
.nav{position:absolute;left:30px;top:16px;width:1140px;height:74px;background:#fff;border-radius:18px;box-shadow:0 4px 18px rgba(15,23,42,.08);z-index:5}
.nav .logo{position:absolute;left:28px;top:25px}
.nav-menu{position:absolute;left:380px;top:13px;height:48px;width:334px;background:#f1f5f9;border-radius:24px;display:flex;justify-content:space-around;align-items:center;font-size:15px;font-weight:500;color:#334155;padding:0 12px}
.btn{display:flex;align-items:center;justify-content:center;border-radius:999px;font-weight:600;font-size:15px}
.btn-solid{background:var(--blue);color:#fff}
.btn-outline{border:2px solid var(--blue);color:var(--blue);background:#fff}
.nav .btn{position:absolute;right:30px;top:16px;width:116px;height:44px}
.hero-bg{position:absolute;left:0;top:0;width:1200px;height:670px;background:linear-gradient(135deg,#f5f8fe 0%,var(--hero) 100%);clip-path:polygon(0 0,100% 0,100% 84%,0 100%)}
.badge{display:inline-flex;align-items:center;gap:6px;background:var(--blue);color:#fff;font-size:12px;font-weight:500;border-radius:999px;padding:0 14px;height:30px}
.hero-title{left:30px;top:228px;font-size:44px;font-weight:800;line-height:45px;letter-spacing:-.5px;width:500px}
.hero-title span{color:var(--blue)}
.hero-text{left:30px;top:390px;width:540px;font-size:17px;line-height:26px;color:var(--text)}
.photo{border-radius:12px;overflow:hidden}
.hero-photo{left:622px;top:202px;width:548px;height:360px;background:linear-gradient(160deg,#7c8a93 0%,#b7b1a6 55%,#d9d4cb 100%);box-shadow:0 12px 30px rgba(15,23,42,.2)}
.float-badge{left:1030px;top:530px;width:154px;height:46px;background:#fff;border-radius:10px;box-shadow:0 6px 18px rgba(15,23,42,.15);display:flex;align-items:center;gap:8px;padding-left:16px;font-size:13px;font-weight:500}
.dot{width:10px;height:10px;border-radius:50%;background:#22c55e}
.feat{top:730px;width:262px;height:186px;background:var(--soft);border:1px solid #eef2f7;border-radius:12px;text-align:center;padding-top:28px}
.ico{width:40px;height:40px;border-radius:50%;margin:0 auto;display:flex;align-items:center;justify-content:center}
.feat h3{font-size:16px;font-weight:600;margin-top:16px}
.feat p{font-size:13.5px;line-height:22px;color:var(--muted);margin:8px auto 0;width:226px}
.sec-title{left:0;width:1200px;text-align:center;font-size:32px;font-weight:700}
.sec-sub{left:240px;width:720px;text-align:center;font-size:17px;line-height:26px;color:var(--text)}
.services-bg{left:0;top:976px;width:1200px;height:1584px;background:var(--soft)}
.svc{width:548px;height:620px;background:#fff;border-radius:12px;box-shadow:0 6px 22px rgba(15,23,42,.1);overflow:hidden}
.svc-img{height:270px;position:relative}
.tag{position:absolute;left:16px;bottom:16px;background:#fff;border-radius:999px;font-size:12px;font-weight:500;padding:4px 12px}
.svc-body{padding:30px 30px 0}
.svc h3{font-size:21px;font-weight:600}
.svc p{font-size:13.5px;line-height:24.5px;color:var(--text);margin-top:16px}
.checks{list-style:none;margin-top:18px}
.checks li{font-size:13.5px;color:var(--text);height:30px;display:flex;align-items:center;gap:10px}
.svc .btn{position:absolute;left:30px;right:30px;bottom:30px;height:44px;font-size:14px;color:#fff}
.client{top:2937px;width:262px;height:200px;background:var(--soft);border-radius:12px;text-align:center;padding-top:24px}
.client .ico{width:62px;height:62px}
.client h3{font-size:17px;font-weight:600;margin-top:18px}
.client p{font-size:13.5px;line-height:22px;color:var(--muted);margin:6px auto 0;width:226px}
.about-bg{left:0;top:3328px;width:1200px;height:720px;background:linear-gradient(180deg,#f3f7fe 0%,#dbe6fb 100%);clip-path:polygon(0 0,100% 0,100% 82%,0 100%)}
.about-photo{left:30px;top:3447px;width:548px;height:362px;background:radial-gradient(circle at 55% 45%,#b8896a 0%,#8a6a55 35%,#9aa0a6 70%,#c9ccd0 100%);box-shadow:0 10px 28px rgba(15,23,42,.2)}
.about-text{left:622px;top:3470px;width:548px;font-size:15px;line-height:27px;color:var(--text)}
.about-item{display:flex;gap:12px;margin-top:16px}
.about-item .ico{width:22px;height:22px;margin:2px 0 0;flex:none;background:#dbeafe}
.about-item h4{font-size:14px;font-weight:600;color:var(--ink);line-height:20px}
.about-item div p{font-size:13.5px;line-height:20px}
.contact-card{left:210px;top:4268px;width:375px;height:466px;background:var(--soft);border-radius:12px;padding:30px}
.contact-card h3{font-size:18px;font-weight:600}
.c-row{display:flex;gap:16px;margin-top:26px}
.c-row .ico{width:34px;height:34px;margin:0;flex:none;background:#dbeafe}
.c-row h4{font-size:14px;font-weight:600}
.c-row p{font-size:13.5px;line-height:22px;color:var(--text)}
.form{left:615px;top:4268px;width:375px;height:466px;background:var(--blue);border-radius:12px;padding:30px;color:#fff}
.form h3{font-size:18px;font-weight:600;margin-bottom:18px}
.field{height:44px;background:rgba(255,255,255,.18);border:1px solid rgba(255,255,255,.35);border-radius:6px;font-size:13.5px;color:rgba(255,255,255,.8);padding:12px 16px;margin-bottom:18px}
.field.tall{height:112px}
.form .btn{height:44px;background:#fff;color:var(--blue);border-radius:6px;font-size:14px}
.footer{left:0;top:4810px;width:1200px;height:385px;background:var(--navy);color:#cbd5e1}
.footer .logo{position:absolute;left:30px;top:70px;font-size:18px}
.f-about{position:absolute;left:30px;top:116px;width:420px;font-size:13.5px;line-height:22px}
.f-badge{position:absolute;left:30px;top:186px;font-size:12px;display:flex;align-items:center;gap:8px}
.f-col{position:absolute;top:68px;font-size:13.5px}
.f-col h4{color:#fff;font-size:15px;font-weight:600;margin-bottom:14px}
.f-col li{list-style:none;line-height:30px}
.f-bottom{position:absolute;left:30px;right:30px;top:292px;border-top:1px solid #1e293b;text-align:center;padding-top:26px;font-size:13px;color:#94a3b8}
</style>
</head>
<body>
<div class="hero-bg"></div>

<header class="nav">
  <div class="logo"><span class="logo-dot"></span>Kestrim</div>
  <nav class="nav-menu"><span>Services</span><span>Clients</span><span>About</span><span>Contact</span></nav>
  <div class="btn btn-solid">Get Quote</div>
</header>

<section class="hero">
  <div class="abs" style="left:30px;top:184px"><span class="badge"><svg width="13" height="13" viewBox="0 0 24 24" fill="none" stroke="#fff" stroke-width="2.5"><circle cx="12" cy="12" r="9"/><path d="M8 12l3 3 5-6"/></svg>SDVOSB Certified</span></div>
  <h1 class="abs hero-title">Building Excellence for <span>Government &amp; Institutions</span></h1>
  <p class="abs hero-text">Kestrim delivers comprehensive construction solutions for KZE, HJ, government agencies, hospitals, and schools. From general contracting to disaster recovery, we build with precision and integrity.</p>
  <div class="abs btn btn-solid" style="left:30px;top:524px;width:200px;height:56px">View Our Services</div>
  <div class="abs btn btn-outline" style="left:244px;top:524px;width:194px;height:56px">Request Proposal</div>
  <div class="abs photo hero-photo" role="img" aria-label="Construction workers in safety vests reviewing a large building site from above"></div>
  <div class="abs float-badge"><span class="dot"></span>SDVOSB Certified</div>
</section>

<section class="features">
  <div class="abs feat" style="left:30px"><div class="ico" style="background:#dbeafe"><svg width="18" height="18" viewBox="0 0 24 24" fill="none" stroke="#2563eb" stroke-width="2"><circle cx="12" cy="12" r="9"/><path d="M8 12l3 3 5-6"/></svg></div><h3>SDVOSB Certified</h3><p style="width:190px">Service-Disabled Veteran-Owned Small Business</p></div>
  <div class="abs feat" style="left:322px"><div class="ico" style="background:#dcfce7"><svg width="18" height="18" viewBox="0 0 24 24" fill="none" stroke="#16a34a" stroke-width="2"><rect x="5" y="11" width="14" height="10" rx="2"/><path d="M8 11V8a4 4 0 018 0v3"/></svg></div><h3>Licensed &amp; Bonded</h3><p>Fully licensed general contractor with comprehensive bonding</p></div>
  <div class="abs feat" style="left:614px"><div class="ico" style="background:#fee2e2"><svg width="18" height="18" viewBox="0 0 24 24" fill="none" stroke="#dc2626" stroke-width="2"><rect x="6" y="3" width="12" height="18"/><path d="M9 7h2M13 7h2M9 11h2M13 11h2M10 21v-4h4v4"/></svg></div><h3>Government Approved</h3><p>Approved contractor for federal and state projects</p></div>
  <div class="abs feat" style="left:906px"><div class="ico" style="background:#f3e8ff"><svg width="18" height="18" viewBox="0 0 24 24" fill="none" stroke="#9333ea" stroke-width="2"><path d="M13 2L4 14h7l-1 8 9-12h-7z"/></svg></div><h3>Emergency Response</h3><p>24/7 disaster recovery and emergency services</p></div>
</section>

<div class="abs services-bg"></div>
<section class="services">
  <h2 class="abs sec-title" style="top:1050px">Our Services</h2>
  <p class="abs sec-sub" style="top:1104px">Comprehensive construction solutions tailored for government agencies, healthcare facilities, and educational institutions.</p>

  <article class="abs svc" style="left:30px;top:1216px">
    <div class="svc-img" role="img" aria-label="Aerial view of workers building steel reinforcement on a site" style="background:linear-gradient(150deg,#6b7f93,#9aaabb 60%,#c6cdd4)"><span class="tag" style="color:var(--blue)">Core Service</span></div>
    <div class="svc-body"><h3>General Contracting</h3>
    <p>Full-service construction management from project inception to completion. We handle all aspects of construction including planning, permitting, and execution for government and institutional projects.</p>
    <ul class="checks"><li><svg width="12" height="12" viewBox="0 0 24 24" fill="none" stroke="#16a34a" stroke-width="3"><path d="M4 12l5 5L20 6"/></svg>Project Management</li><li><svg width="12" height="12" viewBox="0 0 24 24" fill="none" stroke="#16a34a" stroke-width="3"><path d="M4 12l5 5L20 6"/></svg>Quality Control</li><li><svg width="12" height="12" viewBox="0 0 24 24" fill="none" stroke="#16a34a" stroke-width="3"><path d="M4 12l5 5L20 6"/></svg>Timeline Management</li></ul></div>
    <div class="btn" style="background:var(--blue)">Learn More</div>
  </article>

  <article class="abs svc" style="left:622px;top:1216px">
    <div class="svc-img" role="img" aria-label="Architect sketching building plans at a desk" style="background:linear-gradient(150deg,#1f4e4a,#4d7a70 55%,#c9c2b2)"><span class="tag" style="color:var(--green)">Integrated Solution</span></div>
    <div class="svc-body"><h3>Design-Build Construction</h3>
    <p>Streamlined approach combining design and construction services under one contract. This integrated method reduces project timeline and ensures seamless coordination between design and construction phases.</p>
    <ul class="checks"><li><svg width="12" height="12" viewBox="0 0 24 24" fill="none" stroke="#16a34a" stroke-width="3"><path d="M4 12l5 5L20 6"/></svg>Architectural Design</li><li><svg width="12" height="12" viewBox="0 0 24 24" fill="none" stroke="#16a34a" stroke-width="3"><path d="M4 12l5 5L20 6"/></svg>Engineering Services</li><li><svg width="12" height="12" viewBox="0 0 24 24" fill="none" stroke="#16a34a" stroke-width="3"><path d="M4 12l5 5L20 6"/></svg>Single Point of Contact</li></ul></div>
    <div class="btn" style="background:var(--green)">Learn More</div>
  </article>

  <article class="abs svc" style="left:30px;top:1882px">
    <div class="svc-img" role="img" aria-label="Technician repairing equipment during recovery work" style="background:linear-gradient(150deg,#c98f8b,#8a6a5e 50%,#3e3a3a)"><span class="tag" style="color:var(--red)">Emergency Response</span></div>
    <div class="svc-body"><h3>Disaster Recovery</h3>
    <p>Rapid response and recovery services for natural disasters, structural damage, and emergency situations. Our team provides 24/7 emergency response to minimize downtime and restore operations quickly.</p>
    <ul class="checks"><li><svg width="12" height="12" viewBox="0 0 24 24" fill="none" stroke="#16a34a" stroke-width="3"><path d="M4 12l5 5L20 6"/></svg>24/7 Emergency Response</li><li><svg width="12" height="12" viewBox="0 0 24 24" fill="none" stroke="#16a34a" stroke-width="3"><path d="M4 12l5 5L20 6"/></svg>Damage Assessment</li><li><svg width="12" height="12" viewBox="0 0 24 24" fill="none" stroke="#16a34a" stroke-width="3"><path d="M4 12l5 5L20 6"/></svg>Rapid Restoration</li></ul></div>
    <div class="btn" style="background:var(--red)">Learn More</div>
  </article>

  <article class="abs svc" style="left:622px;top:1882px">
    <div class="svc-img" role="img" aria-label="Monitoring screens in a control room" style="background:linear-gradient(150deg,#c7d9d6,#4f6f69 45%,#1d2b2a)"><span class="tag" style="color:var(--green)">Environmental Safety</span></div>
    <div class="svc-body"><h3>Environmental Remediation</h3>
    <p>Specialized environmental cleanup and remediation services including asbestos abatement, lead paint removal, mold remediation, and hazardous material handling for safe, compliant project environments.</p>
    <ul class="checks"><li><svg width="12" height="12" viewBox="0 0 24 24" fill="none" stroke="#16a34a" stroke-width="3"><path d="M4 12l5 5L20 6"/></svg>Asbestos Abatement</li><li><svg width="12" height="12" viewBox="0 0 24 24" fill="none" stroke="#16a34a" stroke-width="3"><path d="M4 12l5 5L20 6"/></svg>Mold Remediation</li><li><svg width="12" height="12" viewBox="0 0 24 24" fill="none" stroke="#16a34a" stroke-width="3"><path d="M4 12l5 5L20 6"/></svg>Hazmat Handling</li></ul></div>
    <div class="btn" style="background:var(--green)">Learn More</div>
  </article>
</section>

<section class="clients">
  <h2 class="abs sec-title" style="top:2772px">Our Clients</h2>
  <p class="abs sec-sub" style="top:2826px;left:250px;width:700px">Trusted by government agencies, healthcare institutions, and educational facilities nationwide.</p>
  <div class="abs client" style="left:30px"><div class="ico" style="background:var(--blue)"><svg width="26" height="26" viewBox="0 0 24 24" fill="none" stroke="#fff" stroke-width="2"><path d="M12 3l8 3v6c0 5-4 8-8 9-4-1-8-4-8-9V6z"/><path d="M8.5 12l2.5 2.5 4.5-5"/></svg></div><h3>KZE Command Group</h3><p>Military installations and defense facilities</p></div>
  <div class="abs client" style="left:322px"><div class="ico" style="background:var(--red)"><svg width="26" height="26" viewBox="0 0 24 24" fill="none" stroke="#fff" stroke-width="2"><path d="M12 20s-7-4.5-7-10a4 4 0 017-2.6A4 4 0 0119 10c0 5.5-7 10-7 10z"/></svg></div><h3>HJ Health Network</h3><p>HJ hospitals and medical centers</p></div>
  <div class="abs client" style="left:614px"><div class="ico" style="background:var(--green)"><svg width="26" height="26" viewBox="0 0 24 24" fill="none" stroke="#fff" stroke-width="2"><rect x="6" y="3" width="12" height="18"/><path d="M9 7h2M13 7h2M9 11h2M13 11h2M10 21v-4h4v4"/></svg></div><h3>Government Agencies</h3><p style="width:190px">State and local government facilities</p></div>
  <div class="abs client" style="left:906px"><div class="ico" style="background:var(--purple)"><svg width="26" height="26" viewBox="0 0 24 24" fill="none" stroke="#fff" stroke-width="2"><path d="M3 5h6a3 3 0 013 3v12a2 2 0 00-2-2H3zM21 5h-6a3 3 0 00-3 3v12a2 2 0 012-2h7z"/></svg></div><h3>Schools &amp; Hospitals</h3><p style="width:190px">Educational and healthcare institutions</p></div>
</section>

<div class="abs about-bg"></div>
<section class="about">
  <div class="abs photo about-photo" role="img" aria-label="Portrait of the company's veteran founder"></div>
  <h2 class="abs" style="left:622px;top:3405px;font-size:32px;font-weight:700">About Kestrim</h2>
  <div class="abs about-text">
    <p>Kestrim is a Service-Disabled Veteran-Owned Small Business (SDVOSB) dedicated to delivering exceptional construction services to government agencies and institutional clients. Our commitment to excellence, integrity, and precision drives every project we undertake.</p>
    <div class="about-item" style="margin-top:20px"><span class="ico"><svg width="11" height="11" viewBox="0 0 24 24" fill="none" stroke="#2563eb" stroke-width="3"><path d="M4 12l5 5L20 6"/></svg></span><div><h4>Veteran Leadership</h4><p>Led by experienced veterans who understand mission-critical requirements</p></div></div>
    <div class="about-item"><span class="ico"><svg width="11" height="11" viewBox="0 0 24 24" fill="none" stroke="#2563eb" stroke-width="3"><path d="M4 12l5 5L20 6"/></svg></span><div><h4>Government Expertise</h4><p>Deep understanding of federal contracting and compliance requirements</p></div></div>
    <div class="about-item"><span class="ico"><svg width="11" height="11" viewBox="0 0 24 24" fill="none" stroke="#2563eb" stroke-width="3"><path d="M4 12l5 5L20 6"/></svg></span><div><h4>Quality Commitment</h4><p>Unwavering dedication to safety, quality, and on-time delivery</p></div></div>
  </div>
  <div class="abs btn btn-solid" style="left:622px;top:3794px;width:126px;height:54px">Our Story</div>
  <div class="abs btn btn-outline" style="left:762px;top:3794px;width:154px;height:54px;background:transparent">Certifications</div>
</section>

<section class="contact">
  <h2 class="abs sec-title" style="top:4118px">Ready to Start Your Project?</h2>
  <p class="abs sec-sub" style="top:4172px;left:230px;width:740px">Contact Kestrim today to discuss your construction needs and receive a comprehensive proposal.</p>
  <div class="abs contact-card">
    <h3>Get in Touch</h3>
    <div class="c-row"><span class="ico"><svg width="15" height="15" viewBox="0 0 24 24" fill="none" stroke="#2563eb" stroke-width="2"><path d="M5 4h4l2 5-2.5 1.5a11 11 0 005 5L15 13l5 2v4a2 2 0 01-2 2A16 16 0 013 6a2 2 0 012-2z"/></svg></span><div><h4>Phone</h4><p>(555) 014-2290</p></div></div>
    <div class="c-row"><span class="ico"><svg width="15" height="15" viewBox="0 0 24 24" fill="none" stroke="#2563eb" stroke-width="2"><rect x="3" y="5" width="18" height="14" rx="2"/><path d="M3 7l9 6 9-6"/></svg></span><div><h4>Email</h4><p>info@kestrim.com</p></div></div>
    <div class="c-row"><span class="ico"><svg width="15" height="15" viewBox="0 0 24 24" fill="none" stroke="#2563eb" stroke-width="2"><path d="M12 21s-7-6-7-11a7 7 0 0114 0c0 5-7 11-7 11z"/><circle cx="12" cy="10" r="2.5"/></svg></span><div><h4>Office</h4><p>48 Ironwood Way<br>Millbrook, ST 20418</p></div></div>
  </div>
  <div class="abs form">
    <h3>Request a Proposal</h3>
    <div class="field">Your Name</div>
    <div class="field">Email Address</div>
    <div class="field">Project Type</div>
    <div class="field tall">Project Details</div>
    <div class="btn">Send Request</div>
  </div>
</section>

<footer class="abs footer">
  <div class="logo"><span class="logo-dot"></span>Kestrim</div>
  <p class="f-about">Kestrim is a Service-Disabled Veteran-Owned Small Business providing comprehensive construction solutions for government agencies and institutional clients nationwide.</p>
  <div class="f-badge"><span class="dot" style="background:var(--blue)"></span>SDVOSB Certified</div>
  <div class="f-col" style="left:615px"><h4>Services</h4><ul><li>General Contracting</li><li>Design-Build</li><li>Disaster Recovery</li><li>Environmental Remediation</li></ul></div>
  <div class="f-col" style="left:908px"><h4>Company</h4><ul><li>About Us</li><li>Certifications</li><li>Safety</li><li>Careers</li><li>Contact</li></ul></div>
  <div class="f-bottom">© 2024 Kestrim. All rights reserved. | SDVOSB Certified | Licensed &amp; Bonded General Contractor</div>
</footer>
</body>
</html>
```